Marlene's 75th birthday

I need an invitation design for my aunt's 75th birthday party. The event will be created around the theme "Coming Home," and will also serve as a family reunion. We will be using an image of a salmon that she recently had tattooed on her thigh (however PLEASE NOTE: the artwork I'm providing here is very similar but is not the final artwork -- it will be replaced). I've attached the text, which includes a line from a poem that she wrote about the tattoo. You are welcome to rearrange this text if you have a vision that makes more sense. I will most likely work with the winning designer on a second project in a month or so, to create the event program.

```html
<!DOCTYPE html>
<html lang="en">
<head>
<meta charset="utf-8">
<title>Marlene's 75th Birthday – Coming Home</title>
<link rel="stylesheet" href="https://fonts.googleapis.com/css2?family=Lobster+Two:ital,wght@1,400;1,700&display=swap">
<style>
  :root {
    --backdrop: #d9b36e;
    --card-deep: #071a36;
    --card-mid: #0b4a86;
    --card-light: #0a6aa9;
    --wave-tint: rgba(120, 170, 230, 0.10);
    --salmon-art: #2f7cc0;
    --salmon-art-soft: #1d5f9c;
    --ink: #ffffff;
  }
  * { margin: 0; padding: 0; box-sizing: border-box; }
  html, body {
    width: 869px;
    height: 1200px;
    overflow: hidden;
    background: var(--backdrop);
  }
  .invitation {
    position: absolute;
    left: 126px;
    top: 28px;
    width: 631px;
    height: 974px;
    overflow: hidden;
    background: linear-gradient(to bottom, var(--card-deep) 0%, var(--card-mid) 38%, var(--card-light) 100%);
    color: var(--ink);
    text-align: center;
  }
  .wave {
    position: absolute;
    left: 0;
    top: 340px;
    width: 631px;
    height: 634px;
  }
  .salmon-art {
    position: absolute;
    left: 344px;
    top: 40px;
    width: 240px;
    height: 300px;
    border-radius: 55% 45% 40% 60% / 35% 40% 60% 65%;
    background: radial-gradient(ellipse at 50% 40%, var(--salmon-art) 0%, var(--salmon-art-soft) 60%, transparent 100%);
    opacity: 0.55;
    transform: rotate(18deg);
  }
  .poem {
    position: absolute;
    left: 0;
    top: 156px;
    width: 472px;
    font-family: "Lobster Two", cursive;
    font-style: italic;
    font-weight: 400;
    font-size: 19px;
    line-height: 34px;
  }
  .poem-credit {
    font-weight: 700;
    padding-left: 20px;
  }
  .headline, .details {
    position: absolute;
    left: 0;
    width: 631px;
    font-family: "Lobster Two", cursive;
    font-style: italic;
    font-weight: 700;
    font-size: 19px;
    line-height: 29px;
  }
  .headline { top: 401px; }
  .details { top: 516px; }
  .program, .gifts {
    position: absolute;
    left: 0;
    width: 631px;
    font-family: "Lobster Two", cursive;
    font-style: italic;
    font-weight: 400;
    font-size: 18px;
    line-height: 28.6px;
  }
  .program { top: 646px; }
  .gifts { top: 776px; }
</style>
</head>
<body>
  <main class="invitation">
    <svg class="wave" viewBox="0 0 631 634" aria-hidden="true">
      <path d="M0 18 C 60 6, 110 2, 150 4 C 260 10, 340 38, 440 36 C 520 34, 590 26, 631 24 L631 634 L0 634 Z" fill="var(--wave-tint)"/>
    </svg>

    <div class="salmon-art" role="img" aria-label="Illustration of a leaping salmon"></div>

    <blockquote class="poem">
      <p>What a quiet wonder, the many rivers we have crossed</p>
      <p>Family voices, old stories and the shining</p>
      <p>Pull of the current that rises when a child feels</p>
      <p>Salmon so close on their long patient journey home.</p>
      <p class="poem-credit">- Marlene Thornby, River Song</p>
    </blockquote>

    <section class="headline">
      <p>You are warmly invited</p>
      <p>To an intimate family gathering</p>
      <p>In Celebration of Marlene’s 75th Birthday</p>
    </section>

    <section class="details">
      <p>Sunday, February 15, 2015</p>
      <p>5 to 9 pm</p>
      <p>Riverbend Lodge</p>
      <p>418 S.W. Alder Lane, Cedar Falls, Oregon</p>
    </section>

    <section class="program">
      <p>Please join us for a light-hearted evening of limericks and laughter</p>
      <p>Readings by Marlene from the Riverbenders</p>
      <p>Music by Daniel Hollis</p>
      <p>Dinner will be served</p>
    </section>

    <section class="gifts">
      <p>No gifts, please</p>
      <p>But all are invited to bring something that sheds light --</p>
      <p>candles in glass, penlights, miners lamps</p>
      <p>How has it illuminated your path forward,</p>
      <p>Or guided you in coming home?</p>
    </section>
  </main>
</body>
</html>
```